Business Card Design for Mortgage Broking Business

We need to redesign the business card. Mortgage broking business, doing home loan and commercial loans, existing logo, also QLPN member logo. design style needs to be simple, professional, elegant.

once final, need to setup for a team of different names and contact details.

Industry/Entity Type

Loan

Contact Information for Business Card

Name; Mobile; Email; Address; Tel; Fax; Australian Credit Licence: 782316

```html
<!DOCTYPE html>
<html lang="en">
<head>
<meta charset="utf-8">
<title>Harbourline Lending – Business Card</title>
<link href="https://fonts.googleapis.com/css2?family=Open+Sans:wght@400;600;700&display=swap" rel="stylesheet">
<style>
  :root {
    --backdrop: #dcdcdc;
    --card: #ffffff;
    --navy: #243a8f;
    --sky: #1e8fdc;
    --ink: #1b1b1b;
    --muted: #555555;
    --ghost: #f1f1f1;
    --badge-fill: #eaf4d8;
  }
  * { margin: 0; padding: 0; box-sizing: border-box; }
  html, body { width: 1200px; height: 852px; overflow: hidden; }
  body {
    background: var(--backdrop);
    font-family: "Open Sans", Arial, sans-serif;
    position: relative;
  }
  .card {
    position: absolute;
    width: 500px;
    height: 290px;
    background: var(--card);
    border-radius: 18px;
    overflow: hidden;
    box-shadow: 0 6px 18px rgba(0,0,0,0.18);
  }
  .card--front { left: 90px; top: 130px; }
  .card--back { left: 610px; top: 430px; }

  .brand {
    position: absolute;
    display: flex;
    align-items: center;
    gap: 10px;
    color: var(--navy);
    font-weight: 700;
    white-space: nowrap;
  }
  .brand__mark { background: var(--navy); flex: none; }
  .card--front .brand { left: 80px; top: 124px; font-size: 30px; }
  .card--front .brand__mark { width: 30px; height: 30px; }
  .card--back .brand { left: 24px; top: 62px; font-size: 15px; gap: 8px; }
  .card--back .brand__mark { width: 16px; height: 16px; }

  .front-decor {
    position: absolute;
    right: 0; top: 0;
    width: 200px; height: 290px;
    background: linear-gradient(180deg, var(--ghost), #fafafa);
  }

  .holder {
    position: absolute;
    left: 250px; top: 58px;
    width: 140px;
    text-align: center;
  }
  .holder__name { font-size: 14px; font-weight: 700; color: var(--ink); line-height: 18px; }
  .holder__role { font-size: 10px; color: var(--muted); line-height: 14px; }

  .member-badge {
    position: absolute;
    right: 24px; top: 26px;
    width: 92px; height: 30px;
    border: 2px solid var(--navy);
    background: var(--badge-fill);
  }

  .band { position: absolute; left: 0; top: 0; }
  .website {
    position: absolute;
    right: 24px; top: 194px;
    font-size: 11px;
    color: #ffffff;
  }
  .contacts {
    position: absolute;
    left: 22px; bottom: 16px;
    list-style: none;
    color: #ffffff;
    font-size: 11px;
    line-height: 19px;
  }
  .contacts li { display: flex; align-items: center; gap: 8px; white-space: nowrap; }
  .contacts svg { width: 11px; height: 11px; fill: #ffffff; flex: none; }
  .contacts .fax { margin-left: 10px; }
</style>
</head>
<body>

<section class="card card--front">
  <div class="front-decor" role="img" aria-label="Faint decorative brand pattern"></div>
  <div class="brand"><span class="brand__mark"></span>Harbourline Lending</div>
</section>

<section class="card card--back">
  <svg class="band" width="500" height="290" viewBox="0 0 500 290" aria-hidden="true">
    <polygon points="300,182 500,182 500,290 340,290" fill="var(--sky)"/>
    <polygon points="0,214 0,290 350,290 296,182 0,182" fill="var(--navy)"/>
  </svg>

  <div class="brand"><span class="brand__mark"></span>Harbourline Lending</div>

  <div class="holder">
    <p class="holder__name">Your Long Name</p>
    <p class="holder__role">Managing Director</p>
  </div>

  <div class="member-badge" role="img" aria-label="QLPN approved credit adviser badge"></div>

  <p class="website">www.yourwebsite.com</p>

  <ul class="contacts">
    <li>
      <svg viewBox="0 0 12 12"><path d="M2 1h2.5l1 3-1.5 1a6 6 0 0 0 3 3l1-1.5 3 1V11c-5 0-9-4-9-9z"/></svg>
      000 0 0 000 00
      <svg class="fax" viewBox="0 0 12 12"><path d="M3 1h5v3H3zM1 5h10v6H1zm2 2v2h6V7z"/></svg>
      (03) 5550 1200
    </li>
    <li>
      <svg viewBox="0 0 12 12"><path d="M1 2h10v8H1zm1 1 4 3 4-3z"/></svg>
      yourname@yourwebsite.com
    </li>
    <li>
      <svg viewBox="0 0 12 12"><path d="M6 0a4 4 0 0 1 4 4c0 3-4 8-4 8S2 7 2 4a4 4 0 0 1 4-4zm0 2.5A1.5 1.5 0 1 0 6 5.5 1.5 1.5 0 0 0 6 2.5z"/></svg>
      Your long commercial of office address
    </li>
  </ul>
</section>

</body>
</html>
```